Business Card

We need a business card for a fundraising/sales and marketing company called Kelvora Appeals services. The logo colours are Red Black and white. The final design should communicate professional, reliable yet fun and charity minded
Updates

Sorry for the delay. A decision will be made in the next 48 hours. we are stuck between two designs. Kind Regards, Molly Ravenscroft

Industry/Entity Type

Marketing

```html
<!DOCTYPE html>
<html lang="en">
<head>
<meta charset="utf-8">
<title>Kelvora Appeals services – Business Card</title>
<link rel="stylesheet" href="https://fonts.googleapis.com/css2?family=Open+Sans:wght@400;700;800&display=swap">
<style>
  :root {
    --backdrop: #e6e6e6;
    --card: #fafafa;
    --rule: #c9c9c9;
    --ink: #4a4a4a;
    --ink-soft: #6b6b6b;
    --accent: #d0202a;
    --bar: #4d4d4d;
  }
  * { margin: 0; padding: 0; box-sizing: border-box; }
  html, body {
    width: 1200px;
    height: 901px;
    overflow: hidden;
    background: var(--backdrop);
    font-family: "Open Sans", Arial, sans-serif;
  }
  .canvas {
    position: relative;
    width: 1200px;
    height: 901px;
    display: flex;
    align-items: center;
    justify-content: center;
  }
  .business-card {
    position: relative;
    width: 900px;
    height: 514px;
    background: var(--card);
    box-shadow: 0 2px 6px rgba(0,0,0,0.12);
  }
  .divider-line {
    position: absolute;
    left: 0;
    right: 0;
    top: 318px;
    height: 1.5px;
    background: var(--rule);
  }
  .brand {
    position: absolute;
    left: 500px;
    top: 96px;
    display: flex;
    align-items: center;
    gap: 14px;
  }
  .brand-mark {
    width: 30px;
    height: 30px;
    background: var(--accent);
  }
  .brand-name {
    font-weight: 800;
    font-size: 34px;
    letter-spacing: 0.5px;
    color: var(--ink);
    text-transform: uppercase;
  }
  .contact-box {
    position: absolute;
    left: 468px;
    top: 196px;
    width: 372px;
    height: 158px;
    border: 1.5px solid var(--rule);
    background: var(--card);
    padding: 26px 22px;
  }
  .contact-list {
    list-style: none;
    font-size: 16px;
    line-height: 27px;
    color: var(--ink-soft);
  }
  .person {
    position: absolute;
    left: 96px;
    top: 284px;
  }
  .person-name {
    font-weight: 700;
    font-size: 21px;
    color: var(--accent);
    text-transform: uppercase;
    letter-spacing: 0.3px;
  }
  .person-role {
    margin-top: 12px;
    font-size: 15px;
    color: var(--ink-soft);
  }
  .edge-bar {
    position: absolute;
    left: 28px;
    top: 296px;
    width: 34px;
    height: 140px;
    background: var(--bar);
  }
</style>
</head>
<body>
<main class="canvas">
  <article class="business-card">
    <div class="divider-line"></div>
    <div class="brand">
      <span class="brand-mark"></span>
      <span class="brand-name">Kelvora Appeals</span>
    </div>
    <section class="contact-box">
      <ul class="contact-list">
        <li>555 0142 780 3</li>
        <li>Type your address here, 12345</li>
        <li>molly@kelvoraappeals.com</li>
        <li>www.kelvoraappeals.com</li>
      </ul>
    </section>
    <div class="edge-bar"></div>
    <div class="person">
      <h1 class="person-name">Molly Ravenscroft</h1>
      <p class="person-role">Sales promotion</p>
    </div>
  </article>
</main>
</body>
</html>
```